2021 Summer Ads Whitmore Ash Custom Homes

We need a re-design of our summer ad run for our customer, Whitmore Ash Custom Homes. They are custom home builders in the mostly rural parts of West Virginia, USA. They are known for their "Forever Home" tagline. We'd like two designed ads with the main difference being just the custom home that's featured. These designs should be for a Google banner like 300 x 250 and square ad like 250 x 250. For inspiration please visit the Whitmore Ash Custom Homes website at www dot whitmoreashcustomhomes dot com

Target Market(s)

consumers / new home shoppers

Industry/Entity Type

Consumer

Requirements
Must have
• WACH logo
Price Lock Available!
Custom home pic
Learn more >
small QVTG logo mark

```html
<!DOCTYPE html>
<html lang="en">
<head>
<meta charset="utf-8">
<title>Whitmore Ash Custom Homes – Summer Ads</title>
<link href="https://fonts.googleapis.com/css2?family=Montserrat:wght@600;700;800&display=swap" rel="stylesheet">
<style>
:root{
  --sheet:#f7f6f7;
  --white:#ffffff;
  --ink:#141414;
  --brand-red:#c8120f;
  --deep-red:#8f1412;
  --navy:#1d3a7a;
  --home-light:#b9c7b4;
  --home-dark:#6f8a62;
  --barn-light:#b8372c;
  --barn-dark:#8e1f18;
}
*{margin:0;padding:0;box-sizing:border-box}
html,body{width:1200px;height:1030px;overflow:hidden;background:var(--sheet);font-family:"Montserrat",sans-serif}
.ad{position:absolute;background:var(--white);overflow:hidden;box-shadow:0 6px 18px rgba(0,0,0,.08)}
.ad-wide-home{left:114px;top:114px;width:458px;height:381px}
.ad-wide-barn{left:628px;top:114px;width:458px;height:381px}
.ad-square-home{left:114px;top:534px;width:381px;height:381px}
.ad-square-barn{left:628px;top:534px;width:381px;height:381px}
.art{position:absolute;inset:0;width:100%;height:100%}
.brand{position:absolute;display:flex;align-items:center;gap:5px;font-weight:800;font-size:12px;letter-spacing:1px;color:var(--brand-red)}
.brand-mark{width:9px;height:9px;background:var(--brand-red)}
.headline{position:absolute;font-weight:800;font-size:23px;line-height:30px;letter-spacing:2.5px;color:var(--ink);white-space:nowrap}
.cta{position:absolute;width:130px;height:36px;background:var(--brand-red);color:var(--white);border-radius:2px;display:flex;align-items:center;justify-content:center;gap:8px;font-weight:700;font-size:14px}
.cta svg{width:8px;height:12px}
.partner{position:absolute;font-weight:800;font-size:22px;letter-spacing:-.5px;color:var(--navy)}
.partner.small{font-size:17px}
</style>
</head>
<body>

<section class="ad ad-wide-home">
  <svg class="art" viewBox="0 0 458 381" preserveAspectRatio="none">
    <defs><linearGradient id="homeScene" x1="0" y1="0" x2="0" y2="1"><stop offset="0" stop-color="var(--home-light)"/><stop offset="1" stop-color="var(--home-dark)"/></linearGradient></defs>
    <polygon points="0,0 458,0 458,281 282,298 0,229" fill="url(#homeScene)" role="img" aria-label="Rendering of a white board-and-batten custom home with a stone base and two garage doors among trees"/>
    <polygon points="0,229 282,298 458,281 458,260 282,284 0,210" fill="var(--deep-red)" opacity=".85"/>
  </svg>
  <div class="brand" style="left:24px;top:266px"><span class="brand-mark"></span>WHITMORE ASH</div>
  <div class="headline" style="left:24px;top:308px">PRICE LOCK<br>AVAILABLE!</div>
  <div class="cta" style="left:227px;top:317px">Learn More<svg viewBox="0 0 8 12"><path d="M2 1l5 5-5 5" fill="none" stroke="#fff" stroke-width="1.8"/></svg></div>
  <div class="partner small" style="left:380px;top:324px">QVTG</div>
</section>

<section class="ad ad-wide-barn">
  <svg class="art" viewBox="0 0 458 381" preserveAspectRatio="none">
    <defs><linearGradient id="barnScene" x1="0" y1="0" x2="0" y2="1"><stop offset="0" stop-color="var(--barn-light)"/><stop offset="1" stop-color="var(--barn-dark)"/></linearGradient></defs>
    <polygon points="312,0 458,0 458,381 147,381 127,286" fill="url(#barnScene)" role="img" aria-label="Photo of a red board-and-batten garage with white trim and a cupola"/>
    <polygon points="288,0 312,0 152,381 147,381 127,286" fill="var(--brand-red)" opacity=".75"/>
  </svg>
  <div class="brand" style="left:24px;top:30px"><span class="brand-mark"></span>WHITMORE ASH</div>
  <div class="headline" style="left:24px;top:80px">PRICE LOCK<br>AVAILABLE!</div>
  <div class="cta" style="left:24px;top:159px">Learn More<svg viewBox="0 0 8 12"><path d="M2 1l5 5-5 5" fill="none" stroke="#fff" stroke-width="1.8"/></svg></div>
  <div class="partner" style="left:22px;top:312px">QVTG</div>
</section>

<section class="ad ad-square-home">
  <svg class="art" viewBox="0 0 381 381" preserveAspectRatio="none">
    <defs><linearGradient id="homeSceneSq" x1="0" y1="0" x2="0" y2="1"><stop offset="0" stop-color="var(--home-light)"/><stop offset="1" stop-color="var(--home-dark)"/></linearGradient></defs>
    <polygon points="0,0 381,0 381,279 282,298 0,229" fill="url(#homeSceneSq)" role="img" aria-label="Rendering of a white board-and-batten custom home with a stone base and two garage doors among trees"/>
    <polygon points="0,229 282,298 381,279 381,258 282,284 0,210" fill="var(--deep-red)" opacity=".85"/>
  </svg>
  <div class="partner small" style="left:23px;top:22px">QVTG</div>
  <div class="brand" style="left:24px;top:266px"><span class="brand-mark"></span>WHITMORE ASH</div>
  <div class="headline" style="left:24px;top:308px">PRICE LOCK<br>AVAILABLE!</div>
  <div class="cta" style="left:227px;top:317px">Learn More<svg viewBox="0 0 8 12"><path d="M2 1l5 5-5 5" fill="none" stroke="#fff" stroke-width="1.8"/></svg></div>
</section>

<section class="ad ad-square-barn">
  <svg class="art" viewBox="0 0 381 381" preserveAspectRatio="none">
    <defs><linearGradient id="barnSceneSq" x1="0" y1="0" x2="0" y2="1"><stop offset="0" stop-color="var(--barn-light)"/><stop offset="1" stop-color="var(--barn-dark)"/></linearGradient></defs>
    <polygon points="309,0 381,0 381,381 138,381 118,289" fill="url(#barnSceneSq)" role="img" aria-label="Photo of a red board-and-batten garage with white trim and a cupola"/>
    <polygon points="285,0 309,0 143,381 138,381 118,289" fill="var(--brand-red)" opacity=".75"/>
  </svg>
  <div class="brand" style="left:24px;top:26px"><span class="brand-mark"></span>WHITMORE ASH</div>
  <div class="headline" style="left:24px;top:76px">PRICE LOCK<br>AVAILABLE!</div>
  <div class="cta" style="left:24px;top:151px">Learn More<svg viewBox="0 0 8 12"><path d="M2 1l5 5-5 5" fill="none" stroke="#fff" stroke-width="1.8"/></svg></div>
  <div class="partner" style="left:22px;top:312px">QVTG</div>
</section>

</body>
</html>
```